TrellisCover Mobile App needs a new skin

We need to add some sparkle to our mobile application. The app is already built with some of the functionality, screens and components (vanilla material design) and now it needs some styling and inspiration. The application simplifies insurance form capturing and communication to/from the broker. Further to that it has some value added services.

Industry/Entity Type

Insurance Broker

Font styles to use
Sans Serif

Requirements
Must have
• Modern, friendly styling and colors. Material design principles.
Nice to have
• Thinking of a themed background photo with the form elements in a more glassy / semi transparent style.
• Would like to use the same app for some customers as a white labeled version, then just change the themed background image, logo and select dark or light theme for them.

```html
<!DOCTYPE html>
<html lang="en">
<head>
<meta charset="utf-8">
<title>TrellisCover app screens</title>
<link href="https://fonts.googleapis.com/css2?family=Lato:wght@300;400;700&display=swap" rel="stylesheet">
<style>
:root{
  --page:#f0f0f0;
  --navy-top:#2c3d63;
  --navy-bottom:#1c2742;
  --ink:#2b3040;
  --muted:#8b8f99;
  --sky:#a9dcf5;
  --sky-line:#2fb6f0;
  --azure:#00aeef;
  --sand:#f5efbf;
  --sand-dark:#dcd69d;
  --sand-ink:#4a4628;
  --panel:#ececec;
  --tabbar:#e2e2e2;
  --white:#ffffff;
  --danger:#ff3d00;
  --logo-disc:#bfe6f6;
}
*{box-sizing:border-box;margin:0;padding:0}
html,body{width:919px;height:1200px;overflow:hidden;background:var(--page);font-family:"Lato",sans-serif}
.canvas{position:relative;width:919px;height:1200px}
.screen{position:absolute;width:270px;height:476px;overflow:hidden;box-shadow:0 2px 10px rgba(0,0,0,.12)}
.col1{left:27px}.col2{left:324px}.col3{left:621px}
.row1{top:82px}.row2{top:642px}
.dark{background:linear-gradient(180deg,var(--navy-top),var(--navy-bottom));color:var(--white)}
.light{background:var(--panel);color:var(--ink)}
.status{position:absolute;top:0;left:0;right:0;height:18px;display:flex;justify-content:space-between;align-items:center;padding:0 8px;font-size:7px}
.light .status{background:var(--white);color:var(--ink)}
.battery{display:inline-block;width:14px;height:6px;background:currentColor;border-radius:1px;margin-left:3px;vertical-align:middle}
.abs{position:absolute}
.photo{position:absolute;inset:0;background:linear-gradient(180deg,#3d5680 0%,#566b86 35%,#8a6f58 62%,#6d4a33 85%,#5a3b28 100%)}
.brand{position:absolute;left:0;right:0;text-align:center}
.brand-disc{position:absolute;left:50%;width:94px;height:94px;margin-left:-47px;border-radius:50%;background:var(--logo-disc);border:5px solid var(--white)}
.brand-name{font-weight:300;font-size:21px;color:var(--white);letter-spacing:.2px}
.spinner{position:absolute;left:120px;top:367px;width:30px;height:30px;border-radius:50%;border:2px solid rgba(255,255,255,.25);border-top-color:rgba(255,255,255,.85)}
.field{position:absolute;left:23px;width:224px;height:40px;background:var(--white);font-size:12px;color:#9aa7c2;padding:0 10px;display:flex;align-items:center;font-weight:300}
.btn{position:absolute;display:flex;align-items:center;justify-content:center;font-weight:700;font-size:11.5px;text-transform:uppercase}
.btn-sky{background:var(--sky);color:var(--navy-bottom)}
.btn-azure{background:var(--azure);color:var(--white)}
.note{position:absolute;left:0;right:0;text-align:center;font-size:10.5px;font-weight:300;line-height:1.4}
.note a{color:var(--azure);text-decoration:underline}
.legal{position:absolute;left:0;right:0;text-align:center;font-size:5.5px;line-height:1.35;opacity:.75}
.rule{position:absolute;left:23px;right:23px;height:1px;background:rgba(255,255,255,.25)}
.header{position:absolute;top:18px;left:0;right:0;height:53px;background:var(--white);display:flex;align-items:center;justify-content:center;font-weight:300;font-size:21px;color:#555a66}
.back{position:absolute;left:12px;top:16px;width:22px;height:22px}
.card{position:absolute;left:12px;right:14px;padding:6px 9px}
.card h3{font-size:10.5px;font-weight:700;color:var(--ink);margin-bottom:4px}
.card p{font-size:7px;line-height:1.35;color:#5c5a48}
.card-sand{background:var(--sand)}
.card-white{background:var(--white)}
.card-msg{background:var(--white);border-left:3px solid var(--azure)}
.card-msg p{color:#6b6f78}
.btn-sand{left:12px;right:14px;background:var(--sand-dark);color:var(--sand-ink);font-size:10.5px}
.white-zone{position:absolute;left:0;right:0;top:365px;bottom:48px;background:var(--white)}
.tabbar{position:absolute;left:0;right:0;bottom:0;height:48px;background:var(--tabbar);display:flex;justify-content:space-around;align-items:center;padding:0 18px}
.tab{width:30px;height:30px}
.label{position:absolute;left:12px;font-size:11px;color:#aaaeb6;font-weight:300}
.input{position:absolute;left:12px;right:14px;background:var(--white);font-size:12px;color:var(--ink);padding:0 10px;display:flex;align-items:center;line-height:1.3}
.yellow-tip{position:absolute;left:12px;right:14px;background:var(--sand);font-size:7px;color:#5c5a48;display:flex;align-items:center;justify-content:center}
</style>
</head>
<body>
<div class="canvas">

<svg width="0" height="0" style="position:absolute">
  <defs>
    <symbol id="i-home" viewBox="0 0 30 30"><circle cx="15" cy="15" r="13.5" fill="none" stroke="currentColor" stroke-width="1.3"/><path d="M8 15 L15 8.5 L22 15 M10 13.5 V21.5 H13.5 V17 H16.5 V21.5 H20 V13.5" fill="none" stroke="currentColor" stroke-width="1.3" stroke-linejoin="round"/></symbol>
    <symbol id="i-shield" viewBox="0 0 30 30"><circle cx="15" cy="15" r="13.5" fill="none" stroke="currentColor" stroke-width="1.3"/><path d="M15 7.5 L21.5 10 V15 C21.5 19 18.5 21.5 15 23 C11.5 21.5 8.5 19 8.5 15 V10 Z" fill="none" stroke="currentColor" stroke-width="1.3" stroke-linejoin="round"/></symbol>
    <symbol id="i-aid" viewBox="0 0 30 30"><circle cx="15" cy="15" r="13.5" fill="none" stroke="currentColor" stroke-width="1.3"/><g fill="none" stroke="currentColor" stroke-width="1.3"><rect x="6.5" y="12" width="17" height="6" rx="3" transform="rotate(45 15 15)"/><rect x="6.5" y="12" width="17" height="6" rx="3" transform="rotate(-45 15 15)"/></g></symbol>
    <symbol id="i-user" viewBox="0 0 30 30"><circle cx="15" cy="15" r="13.5" fill="none" stroke="currentColor" stroke-width="1.3"/><circle cx="15" cy="12" r="4" fill="none" stroke="currentColor" stroke-width="1.3"/><path d="M8.5 23 C9.5 18.5 12 17 15 17 C18 17 20.5 18.5 21.5 23" fill="none" stroke="currentColor" stroke-width="1.3"/></symbol>
  </defs>
</svg>

<!-- Splash -->
<section class="screen col1 row1">
  <div class="photo" role="img" aria-label="Blurred city skyline photo at dusk"></div>
  <div class="status" style="color:#fff"><span>●●●●● NOVA</span><span>4:21 PM</span><span>100%<i class="battery"></i></span></div>
  <div class="brand-disc" style="top:177px"></div>
  <div class="brand" style="top:278px"><span class="brand-name">trelliscover</span></div>
  <div class="spinner"></div>
</section>

<!-- Create account -->
<section class="screen col2 row1 dark">
  <div class="status"><span>●●●●● NOVA</span><span>4:21 PM</span><span>100%<i class="battery"></i></span></div>
  <div class="brand-disc" style="top:60px"></div>
  <div class="brand" style="top:160px"><span class="brand-name">trelliscover</span></div>
  <div class="field" style="top:217px">first name</div>
  <div class="field" style="top:263px">last name</div>
  <div class="field" style="top:309px">mobile number</div>
  <div class="btn btn-sky" style="left:23px;width:224px;top:354px;height:40px">Create account</div>
  <p class="note" style="top:418px">Already have account? <a>Sign in</a> here</p>
  <p class="legal" style="top:446px">trellis cover v.01.1a. Copyright 2016.<br>All rights reserved</p>
</section>

<!-- Verify pin -->
<section class="screen col3 row1 dark">
  <div class="status"><span>●●●●● NOVA</span><span>4:21 PM</span><span>100%<i class="battery"></i></span></div>
  <div class="brand-disc" style="top:60px"></div>
  <div class="brand" style="top:160px"><span class="brand-name">trelliscover</span></div>
  <div class="rule" style="top:206px"></div>
  <p class="note" style="top:230px;padding:0 26px;font-size:11px">To verify your account, Please enter the pin code we sent to you via SMS</p>
  <div class="rule" style="top:275px"></div>
  <div class="field" style="top:297px">pin code</div>
  <div class="btn btn-sky" style="left:23px;width:224px;top:344px;height:38px;border-bottom:3px solid var(--sky-line)">Sign in</div>
  <div class="btn btn-azure" style="left:23px;width:224px;top:389px;height:40px">Re-send code</div>
  <p class="legal" style="top:446px">trellis cover v.01.1a. Copyright 2016.<br>All rights reserved</p>
</section>

<!-- Home -->
<section class="screen col1 row2 light">
  <div class="status"><span>●●●●● NOVA</span><span>4:21 PM</span><span>100%<i class="battery"></i></span></div>
  <div class="header">trelliscover</div>
  <div class="card card-sand" style="top:85px;height:66px"><h3>Emergency</h3><p>Lorem ipsum dolor sit amet, consectetuer adipiscing elit, sed diam nonummy nibh euismod tincidunt ut laoreet dolore magna aliquam erat volutpat. Ut wisi enim ad</p></div>
  <div class="btn btn-sand" style="top:151px;height:33px">Send S.O.S</div>
  <div class="card card-sand" style="top:195px;height:68px"><h3>Road ride Assistance</h3><p>Lorem ipsum dolor sit amet, consectetuer adipiscing elit, sed diam nonummy nibh euismod tincidunt ut laoreet dolore magna aliquam erat volutpat. Ut wisi enim ad</p></div>
  <div class="btn btn-sand" style="top:263px;height:32px">Request assistance</div>
  <div class="card card-msg" style="top:306px;height:47px"><h3>Message from broker</h3><p>Lorem ipsum dolor sit amet, consectetuer adipiscing elit,</p></div>
  <div class="card card-msg" style="top:366px;height:48px"><h3>Message from insurer</h3><p>Lorem ipsum dolor sit amet, consectetuer adipiscing elit,</p></div>
  <nav class="tabbar">
    <svg class="tab" style="color:var(--azure)"><use href="#i-home"/></svg>
    <svg class="tab" style="color:#444"><use href="#i-shield"/></svg>
    <svg class="tab" style="color:#444"><use href="#i-aid"/></svg>
    <svg class="tab" style="color:#444"><use href="#i-user"/></svg>
  </nav>
</section>

<!-- Account & policies -->
<section class="screen col2 row2 light">
  <div class="status"><span>●●●●● NOVA</span><span>4:21 PM</span><span>100%<i class="battery"></i></span></div>
  <div class="header">trelliscover</div>
  <div class="card card-white" style="top:85px;height:50px;padding-top:8px"><h3>Mara Lindqvist</h3><p style="color:#666">mara@lindqvist.me</p></div>
  <div class="btn btn-sky" style="left:12px;right:14px;top:135px;height:32px;border-top:2px solid var(--sky-line);font-size:10.5px;color:var(--ink)">Edit profile</div>
  <div class="card card-white" style="top:180px;height:49px;padding-top:8px"><h3>Policy 1234567890</h3><p style="color:#666">Broker: OAKRIDGE BROKERS NORTHVALE</p></div>
  <div class="yellow-tip" style="top:229px;height:21px">*If this is not your policy, You can remove it</div>
  <div class="btn btn-sand" style="top:250px;height:32px">Remove</div>
  <div class="white-zone"></div>
  <div class="btn btn-azure" style="left:12px;right:14px;top:380px;height:31px;font-size:10.5px">Add another policy</div>
  <nav class="tabbar">
    <svg class="tab" style="color:#444"><use href="#i-home"/></svg>
    <svg class="tab" style="color:#444"><use href="#i-shield"/></svg>
    <svg class="tab" style="color:#444"><use href="#i-aid"/></svg>
    <svg class="tab" style="color:var(--azure)"><use href="#i-user"/></svg>
  </nav>
</section>

<!-- Edit profile -->
<section class="screen col3 row2 light">
  <div class="status"><span>●●●●● NOVA</span><span>4:21 PM</span><span>100%<i class="battery"></i></span></div>
  <div class="header">trelliscover
    <svg class="back" viewBox="0 0 22 22"><circle cx="11" cy="11" r="10" fill="none" stroke="#333" stroke-width="1.3"/><path d="M16 11 H6.5 M10.5 7 L6.5 11 L10.5 15" fill="none" stroke="#333" stroke-width="1.3" stroke-linecap="round" stroke-linejoin="round"/></svg>
  </div>
  <span class="label" style="top:81px">first name</span>
  <div class="input" style="top:101px;height:39px">John</div>
  <span class="label" style="top:147px">last name</span>
  <div class="input" style="top:166px;height:40px">Doe</div>
  <span class="label" style="top:213px">email</span>
  <div class="input" style="top:233px;height:39px">john@fieldmail.me</div>
  <span class="label" style="top:279px">address</span>
  <div class="input" style="top:299px;height:54px">14 Birchwood Lane Kestrel Bay<br>WC, 4820</div>
  <div class="white-zone"></div>
  <div class="btn" style="left:12px;width:117px;top:380px;height:31px;background:var(--danger);color:#fff;font-size:10.5px">Log out</div>
  <div class="btn btn-azure" style="left:138px;right:14px;top:380px;height:31px;font-size:10.5px">Update profile</div>
  <nav class="tabbar">
    <svg class="tab" style="color:#444"><use href="#i-home"/></svg>
    <svg class="tab" style="color:#444"><use href="#i-shield"/></svg>
    <svg class="tab" style="color:#444"><use href="#i-aid"/></svg>
    <svg class="tab" style="color:var(--azure)"><use href="#i-user"/></svg>
  </nav>
</section>

</div>
</body>
</html>
```